I need a simple, classy and stylish business card. I would like it to have a black background with white writing. I would like you to use my logo you designed on the front with the word 'Imagery" used underneath it in the same font. On the back I was thinking of the website at the top 'tomverrick.com' Then my social media accounts, Can you use the instagram, Facebook and twitter logo then my handles?
Please let me know what you think.
Regards Tom
Must have
- Website: www.tomverrick.com
- Social media handles..
- Instagram: @Tom_Verrick_Imagery
- Facebook: Tom Verrick Imagery
- Twitter: @Tom_Verrick
- Email: info@tomverick.com
- Phone: 0437 518 293

```html
<!DOCTYPE html>
<html lang="en">
<head>
<meta charset="utf-8">
<title>Tom Verrick Imagery – Business Cards</title>
<link href="https://fonts.googleapis.com/css2?family=Fira+Sans:wght@400;600&display=swap" rel="stylesheet">
<style>
  :root {
    --page-bg: #e6e3df;
    --card-black: #050505;
    --panel-dark: #1c1c1c;
    --panel-light: #3b3b3b;
    --gloss: #4a4a4a;
    --ink-white: #ffffff;
    --ink-soft: #d6d6d6;
  }
  * { box-sizing: border-box; margin: 0; padding: 0; }
  html, body {
    width: 1200px; height: 950px; overflow: hidden;
    background: var(--page-bg);
    font-family: "Fira Sans", Arial, sans-serif;
  }
  .sheet {
    width: 1200px; height: 950px;
    display: flex; flex-direction: column;
    align-items: center; justify-content: center; gap: 50px;
  }
  .card {
    position: relative;
    width: 700px; height: 400px;
    border-radius: 22px;
    background: var(--card-black);
    overflow: hidden;
    box-shadow: 0 10px 26px rgba(0,0,0,.25);
    color: var(--ink-white);
  }
  .brand {
    position: absolute; display: flex; align-items: center; gap: 12px;
    font-weight: 400; color: var(--ink-white); white-space: nowrap;
  }
  .brand-dot { border-radius: 50%; background: var(--ink-white); flex: none; }

  /* front */
  .card-front .gloss-band {
    position: absolute; top: 0; right: 0; width: 230px; height: 100%;
    background: linear-gradient(90deg, var(--card-black) 0%, var(--gloss) 35%, #2a2a2a 70%, #1a1a1a 100%);
  }
  .card-front .brand { left: 120px; top: 170px; font-size: 34px; }
  .card-front .brand-dot { width: 30px; height: 30px; }

  /* back */
  .card-back .brand { left: 36px; top: 180px; font-size: 27px; }
  .card-back .brand-dot { width: 36px; height: 36px; }
  .contact-panel {
    position: absolute; top: 0; right: 0; width: 300px; height: 100%;
    background: linear-gradient(160deg, var(--panel-light) 0%, var(--panel-dark) 60%, #111 100%);
    padding: 88px 32px 0 0;
    text-align: right;
  }
  .person-name { font-size: 30px; font-weight: 600; letter-spacing: 1px; }
  .person-role { font-size: 22px; font-weight: 400; margin-top: 2px; color: var(--ink-soft); }
  .contact-list { list-style: none; margin-top: 20px; }
  .contact-list li {
    display: flex; justify-content: flex-end; align-items: center; gap: 10px;
    font-size: 17px; line-height: 27px; color: var(--ink-soft); white-space: nowrap;
  }
  .contact-icon { width: 16px; height: 16px; flex: none; }
  .contact-icon.plain { border-radius: 50%; background: var(--ink-soft); width: 14px; height: 14px; margin: 0 1px; }
</style>
</head>
<body>
<main class="sheet">
  <section class="card card-front" aria-label="Card front">
    <div class="gloss-band"></div>
    <div class="brand"><span class="brand-dot"></span>Tom Verrick Imagery</div>
  </section>

  <section class="card card-back" aria-label="Card back">
    <div class="brand"><span class="brand-dot"></span>Tom Verrick Imagery</div>
    <div class="contact-panel">
      <p class="person-name">SAM ELLERY</p>
      <p class="person-role">President</p>
      <ul class="contact-list">
        <li>0437 518 293
          <svg class="contact-icon" viewBox="0 0 16 16" aria-hidden="true"><path fill="#d6d6d6" d="M4 1l2.5 3-1.5 2c1 2 2.5 3.5 4.5 4.5l2-1.5 3 2.5-1.5 3C7 14 2 9 1 2.5z"/></svg>
        </li>
        <li>info@tomverick.com
          <svg class="contact-icon" viewBox="0 0 16 16" aria-hidden="true"><g fill="none" stroke="#d6d6d6" stroke-width="1.4"><rect x="1.5" y="3.5" width="13" height="9" rx="1"/><path d="M1.5 4l6.5 5 6.5-5"/></g></svg>
        </li>
        <li>www.tomverrick.com
          <svg class="contact-icon" viewBox="0 0 16 16" aria-hidden="true"><g fill="none" stroke="#d6d6d6" stroke-width="1.4"><circle cx="8" cy="8" r="6.5"/><ellipse cx="8" cy="8" rx="2.8" ry="6.5"/><path d="M1.5 8h13"/></g></svg>
        </li>
        <li>@Tom_Verrick <span class="contact-icon plain"></span></li>
        <li>@TomVerrickImagery <span class="contact-icon plain"></span></li>
        <li>@Tom_Verrick_Imagery <span class="contact-icon plain"></span></li>
      </ul>
    </div>
  </section>
</main>
</body>
</html>
```